Cover design brief for the “Lanterns along the river” collection

This collection aims to publish articles by several authors who are practitioners specializing in sociocracy, a participatory mode of governance that is highly innovative, and even quite subversive of the autocratic way in which companies and public institutions operate. However, this method has been widely and increasingly implemented since its initial development in the Netherlands in the 1970s and 80s. It is currently of particular interest to non-profit and cooperative organizations, citizen projects and intentional communities, as well as IT work teams (due to its proximity to the spirit of Agile methods).
The content is intellectually demanding. It won't be a matter of popularization for promotional purposes, but rather of subjects for reflection or in-depth analysis of practices, and feedback from field experience. Nor is it an academic journal.
The language used for these publications is French.
The target audience is French-speaking Europe and Canada.

Target Market(s)

The collection is aimed both at other practitioners of this method who want to develop their knowledge, and at people interested in the subjects of collective intelligence, cooperation and organization, in response to social, ecological and/or political concerns.

Industry/Entity Type

Training and consultancy

Font styles to use
Sans Serif

Requirements
Must have
• The name of the collection: Lanterns along the river - Weaving a quieter commons Each volume will mention the name of the collection as well as the theme of the volume. First one: Volume 1 - Mapping hidden currents within shared endeavours. Selection criteria: - A singular, recurring visual identity for the volumes in the collection, highlighting its theme. - Appeal to potential readers; arouse curiosity. - Good readability of the text (title and subtitle, authors; presentation on back cover). - Simplicity of design variation for the cover of subsequent volumes (changing only the text). - Reasonable price in relation to a hoped-for circulation of between 100 and 300 copies per volume (the theme is linked to a niche that is still fairly narrow in the French-speaking world).
Nice to have
• Suggested graphic design directions If you have another direction to suggest with convincing arguments, we're open to your proposal. - The name of the collection, and in particular "Lanterns along the river", will be visible at first glance. - The overall visual impression is one of movement and dynamism. - The style will be based on illustration work, such as sketchnotes. - The tone is playful and humorous. For example, it may mirror back to the potential reader the cultural clichés and social norms about power that make the theme "lanterns along the river" a challenge to his or her imagination. As stated in the preface to Volume 1: "Most people are used to social environments where the choice is limited to suffering or fighting against powers that seek in a multitude of ways to put us at their service..."

```html
<!DOCTYPE html>
<html lang="en">
<head>
<meta charset="utf-8">
<title>Lanterns along the river — Volume 1</title>
<link rel="stylesheet" href="https://fonts.googleapis.com/css2?family=Cinzel:wght@400;600;700;900&display=swap">
<style>
  :root {
    --ink: #050505;
    --gold: #e2b33c;
    --gold-light: #f6d46a;
    --gold-deep: #b8841f;
    --white: #f5f5f5;
    --silver: #8a8d92;
  }
  * { margin: 0; padding: 0; box-sizing: border-box; }
  html, body { width: 750px; height: 1200px; overflow: hidden; background: var(--ink); }
  .cover {
    position: relative;
    width: 750px;
    height: 1200px;
    background: var(--ink);
    font-family: "Cinzel", Georgia, serif;
    text-align: center;
    overflow: hidden;
  }
  .author {
    position: absolute; top: 20px; left: 0; right: 0;
    color: var(--white);
    font-weight: 700;
    font-size: 38px;
    letter-spacing: 3px;
  }
  .title-main {
    position: absolute; top: 130px; left: 0; right: 0;
    font-weight: 700;
    font-size: 112px;
    line-height: 1;
    letter-spacing: 2px;
    background: linear-gradient(180deg, var(--gold-light) 0%, var(--gold) 50%, var(--gold-deep) 100%);
    -webkit-background-clip: text; background-clip: text;
    color: transparent;
  }
  .title-rest {
    position: absolute; top: 362px; left: 0; right: 0;
    color: var(--gold);
    font-weight: 400;
    font-size: 54px;
    line-height: 1.2;
    letter-spacing: 2px;
  }
  .collection-line {
    position: absolute; top: 488px; left: 0; right: 0;
    color: var(--gold);
    font-weight: 700;
    font-size: 30px;
    line-height: 1.2;
    letter-spacing: 2px;
  }
  .volume-frame {
    position: absolute; left: 30px; top: 637px;
    width: 690px; height: 88px;
    border: 3px solid var(--gold);
  }
  .volume-label {
    position: absolute; top: -34px; left: 50%;
    transform: translateX(-50%);
    padding: 0 18px;
    background: var(--ink);
    color: var(--gold);
    font-weight: 900;
    font-size: 50px;
    line-height: 1.2;
    white-space: nowrap;
  }
  .volume-theme {
    position: absolute; left: 0; right: 0; top: 36px;
    color: var(--white);
    font-weight: 600;
    font-size: 17px;
    line-height: 1.2;
    white-space: nowrap;
  }
  .hero-visual {
    position: absolute; left: 0; right: 0; top: 760px; bottom: 0;
    background:
      radial-gradient(ellipse 22% 45% at 50% 55%, rgba(226,179,60,0.85) 0%, rgba(184,132,31,0.5) 40%, rgba(0,0,0,0) 75%),
      radial-gradient(ellipse 70% 25% at 50% 85%, rgba(138,141,146,0.55) 0%, rgba(0,0,0,0) 80%),
      linear-gradient(180deg, var(--ink) 0%, #111 70%, #1c1c1c 100%);
  }
</style>
</head>
<body>
  <main class="cover">
    <p class="author">Author’s Name</p>
    <h1 class="title-main">LANTERNS</h1>
    <p class="title-rest">ALONG THE RIVER</p>
    <p class="collection-line">WEAVING A QUIETER COMMONS</p>
    <section class="volume-frame">
      <h2 class="volume-label">VOLUME 1</h2>
      <p class="volume-theme">MAPPING HIDDEN CURRENTS WITHIN SHARED ENDEAVOURS.</p>
    </section>
    <div class="hero-visual" role="img" aria-label="Photograph of a gold chess king standing upright among fallen silver chess pieces on a dark board"></div>
  </main>
</body>
</html>
```